Flask Their Crest needs wedding label designs!

Flask Their Crest is looking for new wedding designs! Please look at http://www.flasktheircrest.example/water-bottle-labels and http://www.flasktheircrest.example/custom-water to get an idea of what we currently offer.

These new designs will be saved onto Flask Their Crest so that customers can come and customize the text and/or add pictures on them for purchase as water bottle labels or custom label bottled water.

Designs must appeal to a broad audience so any and all styles will be considered. Some other sites to draw inspiration from are smallinkwell.example, greetvane.example, vowcardqueens.example and pressfold.example.

Questions? Ask away!

Target Market(s)

Target market is brides, mothers of brides and wedding planners.

Industry/Entity Type

Wedding

Requirements
Must have
• Designs must be at 300 dpi in CMYK. Width is 8.133" Height is 2.377" with a .125" bleed around all sides.

```html
<!DOCTYPE html>
<html lang="en">
<head>
<meta charset="utf-8">
<title>Nadia &amp; Owen – Wedding Bottle Label</title>
<link rel="stylesheet" href="https://fonts.googleapis.com/css2?family=Rye&display=swap">
<style>
  :root {
    --violet: #7f00ff;
    --paper: #ffffff;
    --motif-field: #f1f1ea;
    --frame-line: #837a72;
  }
  html, body {
    margin: 0;
    padding: 0;
    width: 1200px;
    height: 324px;
    overflow: hidden;
    background: var(--paper);
  }
  .label {
    position: relative;
    width: 1200px;
    height: 324px;
    background: var(--paper);
    overflow: hidden;
  }
  .band {
    position: absolute;
    left: 0;
    width: 1200px;
    background: var(--violet);
  }
  .band--top { top: 0; height: 24px; }
  .band--bottom { bottom: 0; height: 27px; }
  .motif-field {
    position: absolute;
    left: 0;
    top: 40px;
    width: 1200px;
    height: 242px;
    background: var(--motif-field);
  }
  .dots {
    position: absolute;
    left: 0;
    width: 1200px;
    height: 6px;
  }
  .dots--top { top: 30px; }
  .dots--bottom { top: 284px; }
  .nameplate {
    position: absolute;
    left: 0;
    top: 0;
    width: 1200px;
    height: 324px;
  }
  .couple-names {
    position: absolute;
    left: 0;
    top: 144px;
    width: 1200px;
    margin: 0;
    text-align: center;
    font-family: "Rye", serif;
    font-weight: 400;
    font-size: 26px;
    line-height: 32px;
    letter-spacing: 1px;
    white-space: nowrap;
    color: var(--violet);
  }
</style>
</head>
<body>
  <div class="label">
    <div class="band band--top"></div>

    <svg class="dots dots--top" viewBox="0 0 1200 6" aria-hidden="true">
      <line x1="3" y1="3" x2="1200" y2="3" stroke="var(--violet)" stroke-width="3" stroke-linecap="round" stroke-dasharray="0 8.5"/>
    </svg>

    <div class="motif-field" role="img" aria-label="Repeating pale grey tile pattern of small flower rosettes in scrolled square frames"></div>

    <svg class="dots dots--bottom" viewBox="0 0 1200 6" aria-hidden="true">
      <line x1="3" y1="3" x2="1200" y2="3" stroke="var(--violet)" stroke-width="3" stroke-linecap="round" stroke-dasharray="0 8.5"/>
    </svg>

    <div class="band band--bottom"></div>

    <svg class="nameplate" viewBox="0 0 1200 324" aria-hidden="true">
      <path fill="var(--paper)" stroke="var(--frame-line)" stroke-width="2.5" stroke-linejoin="round"
        d="M600 72
           C604 80 612 86 624 86
           L704 86
           Q704 100 720 100
           L720 130
           C720 145 730 152 742 159
           C730 166 720 173 720 188
           L720 218
           Q704 218 704 232
           L624 232
           C612 232 604 238 600 246
           C596 238 588 232 576 232
           L496 232
           Q496 218 480 218
           L480 188
           C480 173 470 166 458 159
           C470 152 480 145 480 130
           L480 100
           Q496 100 496 86
           L576 86
           C588 86 596 80 600 72 Z"/>
    </svg>

    <p class="couple-names">NADIA &amp; OWEN</p>
  </div>
</body>
</html>
```